Fresh looking flyer for Vellmar Institute Of Computing

We need a flyer design for our IT school that will be distributed to potential students during our recruitment campaign. We want to feature the following aspects of the school:

-Study IT in a nordic/european way close to your home (design should feel Scandinavian)
-Featuring the dean of the school (photo attached)
-Match the theme of logo (logo attached)
-A potential layout attached as a mockup

CONTENT
* Main Message " LEARN EUROPEAN PROGRAMMING COURSES IN BEKASI"
* Sub Message " 3 MONTH MODULES FROM BEGINNER TO ADVANCED"
* Campaign " ATTEND FREE CLASS & GET 10% OFF COURSE, SIGN UP BETWEEN 7-18MARCH. vellmar.example/free
* Extra info: " GRADUATE AND GET HIRED TO EARN 120 MILLION IDR/YEAR"

End result should be in Adobe Illustrator format.

Target Market(s)

18-30 year old Indonesians interested in IT

Industry/Entity Type

Education

Font styles to use
Sans Serif

Colors
85cae6

Requirements
Must have
• -Photo of the manager
• -Messages as in the project description
• -School logo
• -Nordic look and feel

```html
<!DOCTYPE html>
<html lang="en">
<head>
<meta charset="utf-8">
<title>Vellmar Institute Of Computing – Flyer</title>
<link href="https://fonts.googleapis.com/css2?family=Lato:wght@400;700;900&display=swap" rel="stylesheet">
<style>
  :root {
    --navy: #12406f;
    --sky: #85cae6;
    --sky-light: #a6dcec;
    --periwinkle: #a9c3ea;
    --frame-grey: #8c96a6;
    --frame-blue: #3f5fb5;
    --ink: #333438;
    --white: #ffffff;
  }
  * { box-sizing: border-box; margin: 0; padding: 0; }
  html, body { width: 1200px; height: 789px; overflow: hidden; background: #e9ecef; }
  .flyer {
    position: relative;
    width: 1200px;
    height: 789px;
    overflow: hidden;
    font-family: "Lato", sans-serif;
    background: var(--white);
  }
  .backdrop { position: absolute; inset: 0; }
  .portrait {
    position: absolute;
    left: 700px; top: 40px;
    width: 470px; height: 749px;
    border-radius: 200px 200px 0 0;
    background: linear-gradient(180deg, #d9b9a0 0%, #e8cdb8 38%, #f4f4f4 52%, #ffffff 100%);
  }
  .message {
    position: absolute;
    left: 80px; top: 110px;
    width: 620px;
    text-transform: uppercase;
  }
  .headline {
    color: var(--navy);
    font-weight: 900;
    font-size: 52px;
    line-height: 1.02;
    letter-spacing: 0.5px;
  }
  .subline {
    margin-top: 26px;
    color: var(--ink);
    font-weight: 900;
    font-size: 34px;
    line-height: 1.05;
  }
  .campaign { margin-top: 24px; color: var(--navy); }
  .campaign .small { font-weight: 700; font-size: 23px; line-height: 1.2; }
  .campaign .offer { font-weight: 900; font-size: 40px; line-height: 1.05; }
  .campaign .url {
    display: block;
    margin-top: 6px;
    text-transform: none;
    font-weight: 900;
    font-size: 36px;
    color: var(--navy);
  }
  .footer-band { position: absolute; left: 0; bottom: 0; }
  .brand {
    position: absolute;
    left: 300px; top: 680px;
    display: flex; align-items: center; gap: 18px;
    color: var(--white);
  }
  .brand-dot { width: 22px; height: 22px; border-radius: 50%; background: var(--white); }
  .brand-name {
    font-weight: 400;
    font-size: 28px;
    line-height: 1.1;
    text-transform: uppercase;
    letter-spacing: 1px;
  }
  .salary-pill {
    position: absolute;
    right: 0; top: 560px;
    width: 380px; height: 96px;
    padding: 14px 24px 14px 44px;
    background: var(--navy);
    border-radius: 48px 0 0 48px;
    color: var(--white);
    font-weight: 700;
    font-size: 21px;
    line-height: 1.3;
    text-transform: uppercase;
    display: flex; align-items: center;
  }
</style>
</head>
<body>
<main class="flyer">
  <svg class="backdrop" width="1200" height="789" viewBox="0 0 1200 789" aria-hidden="true">
    <defs>
      <linearGradient id="panel" x1="0" y1="0" x2="0.3" y2="1">
        <stop offset="0" stop-color="#7ec6e2"/>
        <stop offset="0.5" stop-color="#a6dcec"/>
        <stop offset="1" stop-color="#a9c3ea"/>
      </linearGradient>
    </defs>
    <rect x="660" y="0" width="540" height="789" fill="#ffffff"/>
    <polygon points="560,0 1200,0 1200,70 700,120" fill="#3fb8d8"/>
    <rect x="660" y="0" width="26" height="789" fill="var(--frame-grey)"/>
    <polygon points="686,200 860,260 860,640 686,620" fill="#b6d3ee"/>
    <rect x="686" y="470" width="180" height="16" fill="var(--frame-grey)"/>
    <rect x="686" y="80" width="40" height="560" fill="var(--frame-blue)" opacity="0.7"/>
    <polygon points="0,0 660,0 700,789 0,789" fill="url(#panel)"/>
    <polygon points="0,0 420,0 0,300" fill="#ffffff" opacity="0.12"/>
    <polygon points="300,0 660,0 560,260" fill="#ffffff" opacity="0.1"/>
  </svg>

  <div class="portrait" role="img" aria-label="Photo of the school's dean smiling, wearing glasses and a white shirt"></div>

  <section class="message">
    <h1 class="headline">Learn European<br>Programming<br>Courses in Bekasi</h1>
    <p class="subline">3 Month Modules From<br>Beginner to Advanced</p>
    <div class="campaign">
      <p class="small">Attend free class &amp; get</p>
      <p class="offer">10% off course,</p>
      <p class="small">Sign up between 7-18 March</p>
      <span class="url">vellmar.example/free</span>
    </div>
  </section>

  <svg class="footer-band" width="1200" height="789" viewBox="0 0 1200 789" style="top:0" aria-hidden="true">
    <path d="M0,660 C240,620 560,640 720,560 L780,560 L780,789 L0,789 Z" fill="var(--navy)"/>
  </svg>

  <div class="brand">
    <span class="brand-dot"></span>
    <p class="brand-name">Vellmar Institute<br>Of Computing</p>
  </div>

  <p class="salary-pill">Graduate and get hired to<br>earn 120 million IDR/year</p>
</main>
</body>
</html>
```